Letterhead to Prospective Clients

Create a letterhead (word & canva) that I will use to send letters to prospective clients and also include the Coralwood Estate Partners Logo, My Contact Details and Interchangeable "Suburb". Use the same font and colour pallete

Maris Dulworth | "Suburb" Specialist - Redlands & Surrounds
Mobile: 0417 862 095
Email: MD@CoralwoodEstatePartners.com.au

```html
<!DOCTYPE html>
<html lang="en">
<head>
<meta charset="utf-8">
<title>Coralwood Estate Partners — Letterhead</title>
<link href="https://fonts.googleapis.com/css2?family=Arimo:wght@400&family=Mulish:wght@700&display=swap" rel="stylesheet">
<style>
  :root {
    --backdrop: #8d8d8d;
    --paper: #ffffff;
    --ink: #2b2b2b;
    --navy: #1c2533;
    --copper: #d98a3c;
    --rule: #6f6f6f;
  }
  * { box-sizing: border-box; margin: 0; padding: 0; }
  html, body {
    width: 1200px; height: 1159px; overflow: hidden;
    background: var(--backdrop);
  }
  .letterhead {
    position: absolute;
    left: 208px; top: 24px;
    width: 784px; height: 1110px;
    background: var(--paper);
    box-shadow: 0 6px 24px rgba(0,0,0,.35);
    font-family: "Arimo", Arial, sans-serif;
    color: var(--ink);
  }
  .brand {
    position: absolute; top: 104px; left: 0; right: 0;
    display: flex; justify-content: center; align-items: center; gap: 12px;
  }
  .brand-mark {
    width: 14px; height: 14px; border-radius: 50%;
    background: var(--copper);
  }
  .brand-name {
    font-family: "Arimo", Arial, sans-serif;
    font-weight: 400;
    font-size: 26px;
    color: var(--navy);
  }
  .letter {
    position: absolute; top: 330px; left: 96px; right: 96px;
  }
  .salutation {
    font-family: "Mulish", sans-serif;
    font-weight: 700;
    font-size: 17px;
    margin-bottom: 22px;
  }
  .letter p {
    font-size: 14px;
    line-height: 18px;
    margin-bottom: 18px;
  }
  .closing {
    font-family: "Mulish", sans-serif;
    font-weight: 700;
    font-size: 10px;
    margin-top: 36px;
  }
  .signature {
    width: 170px; height: 50px; margin-top: 24px;
    background: linear-gradient(90deg, #ececec, #f6f6f6);
  }
  .footer-rule {
    position: absolute; left: 96px; right: 60px;
    height: 1px; background: var(--rule);
  }
  .footer-rule.top { top: 950px; }
  .footer-rule.bottom { top: 1060px; }
  .contact {
    position: absolute; top: 975px; right: 90px;
    text-align: right; font-size: 15px; color: #444;
  }
  .contact .line { margin-bottom: 8px; white-space: nowrap; }
  .contact .detail { display: inline-flex; align-items: center; gap: 6px; margin-left: 22px; }
  .contact svg { width: 13px; height: 13px; fill: var(--copper); }
</style>
</head>
<body>
  <main class="letterhead">
    <header class="brand">
      <span class="brand-mark" aria-hidden="true"></span>
      <span class="brand-name">Coralwood Estate Partners</span>
    </header>

    <section class="letter">
      <h1 class="salutation">Dear Mr. Smith,</h1>
      <p>Lorem ipsum dolor sit amet, consectetuer adipiscing elit, sed diam nonmmy nibh euismod tincidunt ut laor eet dolore magna aliquam erat volutpat. Ut wisi enim ad minim veniam, quis nostrud exerci tationmcorper suscipit lobortis nisl ut aliquip ex ea commodo consequat. Duis autem vel eum iriure dolor in hendrerit in vulputate velit esse molestie consequat, vel illum dolore eu feugiat</p>
      <p>Rorem ipsum dolor sit amet, consectetuer adipiscing elit, sed diam nonmmy nibh euismod tincidunt ut laor eet dolore magna aliquam erat volutpat. Ut wisi enim ad minim veniam, quis nostrud exerci tationmcorper suscipit lobortis nisl ut aliquip ex ea commodo consequat. Duis autem vel eum iriure dolor in hendrerit in vulputate velit esse molest</p>
      <p>Dorem ipsum dolor sit amet, consectetuer adipiscing elit, sed diam nonmmy nibh euismod tincidunt ut laor eet dolore magna aliquam erat volutpat. Ut wisi enim ad minim veniam, quis nostrud exerci tationmcorper suscipit lobortis nisl ut aliquip ex ea commodo consequat. Duis autem vel eum iriure dolor in hendrerit in suscipit lobortis nisl ut aliquip ex ea commodo consequat. Duis autem vel eum iriure dolor in hendrerit in vulputate velit esse molestie consequat, vel illum</p>
      <p>Sorem ipsum dolor sit amet, consectetuer adipiscing elit, sed diam nonmmy nibh euismod tincidunt ut laor eet dolore magna aliquam erat volutpat. Ut wisi enim ad minim veniam, quis nostrud exerci tationmcorper suscipit lobortis nisl ut aliquip ex ea commodo consequat. Duis autem vel eum iriure dolor in</p>
      <div class="closing">Sincerely,</div>
      <div class="signature" role="img" aria-label="Handwritten signature"></div>
    </section>

    <div class="footer-rule top"></div>
    <footer class="contact">
      <div class="line">Maris Dulworth | "Suburb" Specialist | Redlands &amp; Surrounds</div>
      <div class="line">
        <span class="detail">
          <svg viewBox="0 0 24 24" aria-hidden="true"><path d="M6.6 10.8a15.1 15.1 0 0 0 6.6 6.6l2.2-2.2a1 1 0 0 1 1-.25 11.4 11.4 0 0 0 3.6.57 1 1 0 0 1 1 1V20a1 1 0 0 1-1 1A17 17 0 0 1 3 4a1 1 0 0 1 1-1h3.5a1 1 0 0 1 1 1c0 1.25.2 2.45.57 3.570a1 1 0 0 1-.25 1z"/></svg>
          0417 862 095
        </span>
        <span class="detail">
          <svg viewBox="0 0 24 24" aria-hidden="true"><path d="M2 5h20v14H2zm2 2v.5l8 5 8-5V7l-8 5z"/></svg>
          MD@CoralwoodEstatePartners.com.au
        </span>
      </div>
    </footer>
    <div class="footer-rule bottom"></div>
  </main>
</body>
</html>
```